Transformative School Model Needs a Website. I am easy to work with.

Greetings:
I am creating a K-12 school that is a complete and total re-imagination of what education can be for children, families, communities, and the planet. While we will begin as a K-12 school, I really see it as a complete life cycle education (birth to death). I'm looking for a website to describe my new transformational educational model. I anticipate having 7-8 pages. I have all the copy ready.
I am the Founder. I am easy to work with, an effective communicator, and I’m very good at knowing what I want and providing specific and concrete detail, examples, and direction to make sure I use your time wisely.

```html
<!DOCTYPE html>
<html lang="en">
<head>
<meta charset="utf-8">
<title>Serene Unity Academy</title>
<link href="https://fonts.googleapis.com/css2?family=Cinzel:wght@400;600;700&family=Mulish:wght@400;600;700;800&display=swap" rel="stylesheet">
<style>
:root{
  --orange:#fe4d01;
  --orange-line:#f2531a;
  --yellow:#fdc21a;
  --sky:#72c6e6;
  --ocean:#0b5a86;
  --navy:#0e5479;
  --navy-deep:#0a4463;
  --ink:#2c2c2c;
  --title-blue:#1b7fb0;
  --peach:#fdeee8;
}
*{margin:0;padding:0;box-sizing:border-box}
html,body{width:1200px;height:3976px;overflow:hidden}
body{position:relative;font-family:'Mulish',sans-serif;color:var(--ink);background:#fff}
.abs{position:absolute}
.serif{font-family:'Cinzel',serif}

/* header / hero */
.hero{left:0;top:0;width:1200px;height:730px;background:linear-gradient(100deg,#d9d2c9 0%,#d6cabb 40%,#c99d6c 62%,#bfa58a 78%,#d8d0c6 100%)}
.brand{left:90px;top:-10px;width:200px;height:200px;border-radius:50%;background:#fff;display:flex;align-items:center;justify-content:center;text-align:center;font-family:'Mulish',sans-serif;font-weight:700;font-size:17px;color:var(--title-blue);line-height:1.25;box-shadow:0 2px 10px rgba(0,0,0,.08)}
.nav{left:417px;top:24px;display:flex;gap:23px;font-size:13px;color:#333}
.hero-title{left:105px;top:295px;font-family:'Cinzel',serif;font-weight:600;font-size:59px;line-height:59px;color:#2a2420}
.btn{display:flex;align-items:center;justify-content:space-between;background:var(--orange);color:#fff;border-radius:22px;font-weight:700;font-size:13px;padding:0 8px 0 20px;height:40px}
.btn .dot{width:26px;height:26px;border-radius:50%;background:var(--yellow);display:flex;align-items:center;justify-content:center}
.hero-btn{left:108px;top:486px;width:167px}
.arrow-dot{width:28px;height:28px;border-radius:50%;background:rgba(120,110,100,.55);display:flex;align-items:center;justify-content:center}

/* about */
.about{left:0;top:730px;width:1200px;height:632px;background:linear-gradient(180deg,var(--sky) 0%,#3f9cc7 45%,var(--ocean) 100%)}
.about-title{left:599px;top:818px;font-size:58px;font-weight:600;color:#fff}
.about-copy{left:599px;top:904px;width:489px;font-size:14.5px;line-height:25.8px;color:#fff;text-align:justify}
.about-copy p+p{margin-top:25px}
.founder{left:414px;top:1143px;width:145px;height:40px;border-radius:20px;background:var(--yellow);font-family:'Cinzel',serif;font-size:19px;color:#3a2a00;display:flex;align-items:center;justify-content:center}

/* foundations */
.sec-title{width:1200px;left:0;text-align:center;font-family:'Cinzel',serif;font-weight:600;font-size:46px;background:linear-gradient(180deg,#3aa9d6,#0d5f8c);-webkit-background-clip:text;background-clip:text;color:transparent}
.intro{left:205px;top:1522px;width:790px;text-align:center;font-size:13px;line-height:21.5px;color:#444}
.node-label{font-size:21px;font-weight:600;color:#444;letter-spacing:.5px}
.outcome{top:2223px;width:372px;height:397px}
.caption{top:2632px;width:372px;text-align:center;font-size:26px;font-weight:600;color:#222}
.ghost{left:0;top:2660px;width:1200px;text-align:center;font-family:'Cinzel',serif;font-weight:700;font-size:128px;color:#eef4f8;letter-spacing:2px}

/* testimonials */
.quote{top:2955px;width:306px;height:184px;border:2px solid #333;padding:14px 22px;font-size:13px;line-height:21.6px;color:#666;text-align:justify;background:#fff}
.tail{top:3137px}
.avatar{top:3155px;width:68px;height:68px;border-radius:50%;background:radial-gradient(circle,#c9b5a3 0 45%,#e6e6e6 47%);border:3px solid #f0f0f0}
.who{top:3168px;font-size:17px;color:#333}
.who small{display:block;font-size:12px;color:#6fc3e4;margin-top:2px}
.side-arrow{top:3057px;width:28px;height:28px;border-radius:50%;background:#eee;display:flex;align-items:center;justify-content:center}

/* donate */
.donate-img{left:0;top:3323px;width:536px;height:292px;background:linear-gradient(120deg,#d9cdc6,#c8ada0 55%,#b98c80)}
.donate{left:536px;top:3323px;width:664px;height:292px;background:var(--orange);color:#fff}
.donate h2{position:absolute;left:52px;top:60px;font-family:'Cinzel',serif;font-weight:600;font-size:44px}
.donate p{position:absolute;left:52px;top:124px;width:520px;font-size:13px;line-height:26px}
.donate-btn{left:590px;top:3511px;width:167px;background:var(--yellow)}
.donate-btn .dot{background:var(--orange)}

/* footer */
.footer{left:0;top:3615px;width:1200px;height:265px;background:var(--navy);color:#fff}
.fcol{position:absolute;top:86px}
.fcol h3{font-size:22px;font-weight:800;letter-spacing:.5px;margin-bottom:8px}
.fcol li{list-style:none;font-size:14px;line-height:26px;display:flex;align-items:center;gap:12px}
.social{display:flex;gap:8px;margin-top:4px}
.social span{width:32px;height:32px;background:#fff;border:1px solid #ccc}
.bottom{left:0;top:3880px;width:1200px;height:96px;background:var(--navy-deep);color:#fff;font-size:13px;display:flex;align-items:center;justify-content:center}
</style>
</head>
<body>

<!-- hero -->
<section class="abs hero" role="img" aria-label="Photo of a girl, her mother and grandmother hugging and smiling on a sofa"></section>
<div class="abs brand">Serene<br>Unity<br>Academy</div>
<nav class="abs nav">
  <span>About</span><span>School Foundations</span><span>Curriculum</span><span>Pedagogy</span><span>Outcomes</span><span>Opening</span><span>Testimonials</span><span>Donate</span>
</nav>
<h1 class="abs hero-title">SERENE<br>UNITY<br>ACADEMY</h1>
<a class="abs btn hero-btn">GET STARTED <span class="dot"><svg width="8" height="10" viewBox="0 0 8 10"><path d="M2 1l4 4-4 4" fill="none" stroke="#fe4d01" stroke-width="1.6"/></svg></span></a>
<div class="abs arrow-dot" style="left:111px;top:625px"><svg width="8" height="10" viewBox="0 0 8 10"><path d="M6 1L2 5l4 4" fill="none" stroke="#fff" stroke-width="1.6"/></svg></div>
<div class="abs arrow-dot" style="left:148px;top:625px"><svg width="8" height="10" viewBox="0 0 8 10"><path d="M2 1l4 4-4 4" fill="none" stroke="#fff" stroke-width="1.6"/></svg></div>

<!-- about -->
<section class="abs about"></section>
<svg class="abs" style="left:100px;top:800px" width="470" height="470" viewBox="0 0 470 470">
  <path d="M230 16 A218 218 0 1 0 440 260" fill="none" stroke="#fe4d01" stroke-width="14"/>
  <circle cx="245" cy="231" r="205" fill="#fff"/>
</svg>
<div class="abs" role="img" aria-label="Portrait of the smiling founder in glasses and a blue suit" style="left:140px;top:838px;width:384px;height:384px;border-radius:50%;background:linear-gradient(160deg,#e9ecee 0%,#cfd6dc 45%,#6f8fb0 100%)"></div>
<div class="abs founder">FOUNDER</div>
<h2 class="abs serif about-title">ABOUT ME</h2>
<div class="abs about-copy">
  <p>Lorem ipsum dolor sit amet, consectetur adipiscing elit, sed do eiusmod tempor incididunt ut labore et dolore magna aliqua. Ut enim ad minim veniam, quis nostrud exercitation ullamco laboris nisi ut aliquip ex ea commodo consequat. Duis aute irure dolor in reprehenderit in voluptate velit esse cillum dolore eu fugiat nulla pariatur.</p>
  <p>Excepteur sint occaecat cupidatat non proident, sunt in culpa qui officia deserunt mollit anim id est laborum. Lorem ipsum dolor sit amet, consectetur adipiscing elit, sed do eiusmod tempor incididunt ut labore et dolore magna aliqua. Ut enim ad minim veniam, quis nostrud exercitation ullamco laboris nisi ut aliquip ex ea commodo consequat.</p>
</div>
<a class="abs btn" style="left:599px;top:1217px;width:168px">LEARN MORE <span class="dot"><svg width="8" height="10" viewBox="0 0 8 10"><path d="M2 1l4 4-4 4" fill="none" stroke="#fe4d01" stroke-width="1.6"/></svg></span></a>

<!-- school foundations -->
<h2 class="abs sec-title" style="top:1450px">SCHOOL FOUNDATIONS</h2>
<p class="abs intro">Lorem ipsum dolor sit amet, consectetur adipiscing elit, sed do eiusmod tempor incididunt ut labore et dolore magna aliqua. Ut enim ad minim veniam, quis nostrud exercitation ullamco laboris nisi ut aliquip ex ea commodo consequat. Duis aute irure dolor in reprehenderit in voluptate velit esse cillum dolore eu fugiat nulla pariatur. Excepteur sint occaecat cupidatat non proident, sunt in culpa qui officia deserunt mollit anim id est laborum.</p>

<svg class="abs" style="left:0;top:1640px" width="1200" height="570" viewBox="0 1640 1200 570">
  <g stroke="var(--orange-line)" stroke-width="5" fill="none">
    <line x1="496" y1="1756" x2="702" y2="1755"/>
    <line x1="380" y1="1816" x2="273" y2="1925"/>
    <line x1="818" y1="1816" x2="926" y2="1925"/>
    <line x1="221" y1="2049" x2="221" y2="2199"/>
    <line x1="976" y1="2049" x2="976" y2="2199"/>
  </g>
  <g fill="#fff" stroke="var(--peach)" stroke-width="10">
    <circle cx="426" cy="1763" r="65"/>
    <circle cx="772" cy="1763" r="65"/>
    <circle cx="221" cy="1978" r="65"/>
    <circle cx="976" cy="1978" r="65"/>
  </g>
  <g fill="#fde3d6">
    <circle cx="426" cy="1763" r="26" role="img" aria-label="Grace icon: open hands"/>
    <circle cx="772" cy="1763" r="26" role="img" aria-label="Strength icon: rising arrows"/>
    <circle cx="221" cy="1978" r="26" role="img" aria-label="Wisdom icon: book and light bulb"/>
    <circle cx="976" cy="1978" r="26" role="img" aria-label="Joy icon: smiling faces"/>
  </g>
</svg>
<div class="abs node-label" style="left:360px;top:1655px">GRACE</div>
<div class="abs node-label" style="left:765px;top:1655px">STRENGTH</div>
<div class="abs node-label" style="left:133px;top:1870px">WISDOM</div>
<div class="abs node-label" style="left:971px;top:1870px">JOY</div>
<div class="abs" role="img" aria-label="Photo of two girls hugging in a sunlit forest" style="left:324px;top:1857px;width:553px;height:342px;clip-path:polygon(0 26%,16% 0,84% 0,100% 26%,100% 100%,0 100%);background:linear-gradient(160deg,#8a8a55 0%,#b9a978 40%,#6f6a44 75%,#4f4a32 100%)"></div>

<!-- outcomes -->
<div class="abs outcome" role="img" aria-label="Photo of a smiling woman with curly hair and crossed arms" style="left:19px;background:linear-gradient(170deg,#c9c2b4,#a69988 50%,#2f4a40 85%)"></div>
<div class="abs outcome" role="img" aria-label="Photo of children in a circle looking down at the camera" style="left:415px;background:linear-gradient(180deg,#c8b3a0,#d6b59b 55%,#c3483d 95%)"></div>
<div class="abs outcome" role="img" aria-label="Photo of a smiling man in glasses with a mug and laptop" style="left:811px;background:linear-gradient(160deg,#8a6b52,#6e3c30 45%,#d5d0c8 85%)"></div>
<div class="abs ghost">OUTCOMES</div>
<div class="abs caption" style="left:19px">Self-actualization</div>
<div class="abs caption" style="left:415px">Community-actualization</div>
<div class="abs caption" style="left:811px">Planetary-actualization</div>

<!-- testimonials -->
<h2 class="abs sec-title" style="top:2866px">TESTIMONIALS</h2>
<div class="abs side-arrow" style="left:40px"><svg width="8" height="10" viewBox="0 0 8 10"><path d="M6 1L2 5l4 4" fill="none" stroke="#555" stroke-width="1.6"/></svg></div>
<div class="abs side-arrow" style="left:1130px"><svg width="8" height="10" viewBox="0 0 8 10"><path d="M2 1l4 4-4 4" fill="none" stroke="#555" stroke-width="1.6"/></svg></div>

<div class="abs quote" style="left:111px">Lorem ipsum dolor sit amet, consectetur adipiscing elit, sed do eiusmod tempor incididunt ut labore et dolore magna aliqua. Ut enim ad minim veniam, quis nostrud exercitation ullamco laboris nisi ut aliquip ex ea commodo consequat. Duis aute irure dolor in</div>
<div class="abs quote" style="left:446px">Lorem ipsum dolor sit amet, consectetur adipiscing elit, sed do eiusmod tempor incididunt ut labore et dolore magna aliqua. Ut enim ad minim veniam, quis nostrud exercitation ullamco laboris nisi ut aliquip ex ea commodo consequat. Duis aute irure dolor in</div>
<div class="abs quote" style="left:781px">Lorem ipsum dolor sit amet, consectetur adipiscing elit, sed do eiusmod tempor incididunt ut labore et dolore magna aliqua. Ut enim ad minim veniam, quis nostrud exercitation ullamco laboris nisi ut aliquip ex ea commodo consequat. Duis aute irure dolor in</div>
<svg class="abs tail" style="left:138px" width="30" height="22" viewBox="0 0 30 22"><path d="M2 0 L14 20 L14 0" fill="#fff" stroke="#333" stroke-width="2"/></svg>
<svg class="abs tail" style="left:473px" width="30" height="22" viewBox="0 0 30 22"><path d="M2 0 L14 20 L14 0" fill="#fff" stroke="#333" stroke-width="2"/></svg>
<svg class="abs tail" style="left:808px" width="30" height="22" viewBox="0 0 30 22"><path d="M2 0 L14 20 L14 0" fill="#fff" stroke="#333" stroke-width="2"/></svg>

<div class="abs avatar" role="img" aria-label="Reviewer portrait" style="left:171px"></div>
<div class="abs avatar" role="img" aria-label="Reviewer portrait" style="left:506px"></div>
<div class="abs avatar" role="img" aria-label="Reviewer portrait" style="left:841px"></div>
<div class="abs who" style="left:253px">John Doe<small>Company name</small></div>
<div class="abs who" style="left:588px">John Doe<small>Company name</small></div>
<div class="abs who" style="left:923px">John Doe<small>Company name</small></div>

<!-- donate -->
<div class="abs donate-img" role="img" aria-label="Photo of hands cradling a red heart"></div>
<section class="abs donate">
  <h2>DONATE</h2>
  <p>Lorem ipsum dolor sit amet, consectetur adipiscing elit, sed do eiusmod tempor<br>&nbsp;inc ididunt ut labore et dolore magna aliqua.</p>
</section>
<a class="abs btn donate-btn">DONATE NOW <span class="dot"><svg width="8" height="10" viewBox="0 0 8 10"><path d="M2 1l4 4-4 4" fill="none" stroke="#fff" stroke-width="1.6"/></svg></span></a>

<!-- footer -->
<footer class="abs footer">
  <div class="fcol" style="left:110px">
    <h3>LINKS</h3>
    <ul><li>»&nbsp;Outcomes</li><li>»&nbsp;Opening</li><li>»&nbsp;Testimonials</li><li>»&nbsp;Donate</li></ul>
  </div>
  <div class="fcol" style="left:354px">
    <h3>INFORMATION</h3>
    <ul><li>»&nbsp;About</li><li>»&nbsp;School Foundations</li><li>»&nbsp;Curriculum</li><li>»&nbsp;Pedagogy</li></ul>
  </div>
  <div class="fcol" style="left:648px">
    <h3>SUPPORT</h3>
    <ul>
      <li><svg width="12" height="14" viewBox="0 0 12 14"><path d="M6 13S1 7.5 1 5a5 5 0 0 1 10 0c0 2.5-5 8-5 8z" fill="#fff"/><circle cx="6" cy="5" r="1.8" fill="#0e5479"/></svg>Lorem ipsum dolor sit amet</li>
      <li><svg width="12" height="12" viewBox="0 0 12 12"><path d="M2 1h3l1 3-1.5 1a7 7 0 0 0 3 3L8.5 6.5l3 1v3c0 .5-.5 1-1 1C5 11.5.5 7 .5 2c0-.5.5-1 1.5-1z" fill="#fff"/></svg>+1 888 888 8888</li>
      <li><svg width="12" height="10" viewBox="0 0 12 10"><rect x="0" y="0" width="12" height="10" rx="1" fill="#fff"/><path d="M0 1l6 4 6-4" fill="none" stroke="#0e5479" stroke-width="1.2"/></svg>info@companyname.com</li>
    </ul>
  </div>
  <div class="fcol" style="left:946px">
    <h3>FOLLOW US</h3>
    <div class="social"><span></span><span></span><span></span><span></span></div>
  </div>
</footer>
<div class="abs bottom">© Copyrights Company name 2023. All rights reserved</div>

</body>
</html>
```